New Vidora Channel Banner Graphic/Logo for "Cozy Nook Attic Sound"

Create a banner for my new Vidora channel for Cozy Nook Attic Sound. This is partially a logo project, but the logo will not be used elsewhere. Check out Vidora channels to see the banners others have created. This channel is about my home studio, the gear, microphones, musical instruments, wiring, software etc. that goes into a home studio. It's a free channel, made for sharing information. This is a graphic design that will be posted on vidora using built-in vidora tools.
Updates

More information about this project! I'm staring a channel called "Cozy Nook Attic Sound" on vidorastream.net. I need a deign for this banner and a logo for Cozy Nook Attic Sound. I called the channel by that name because my music studio is my happy place. It's about music and instruments (gutars, piano, drums, percussion) singing (microhpones), creativity, and what you'd expect form musicians. It's also about technology, recording, live-streaming, music videos, etc. It is my hobby, not my profession. I will be creating content for other amateur home studio aficionados and hobbyists. There are a lot of home studio channels and videos you can look at on vidora to get a flavor for musicians and studios. Usually fairly tech-heavy. An appeal of my channel will be a very approachable, "i'm the same as you" welcome for people that are doing it to enjoy it.

I put this project in the wrong category to start. This has been fixed, but I think benefits I would have received (such as invited designers) and announcement of project in the correct category mean I'm not getting designers. Your initial menu should be improved. I'm having a banner created for a web page in Vidora. I think it is easy to mistake that for a web design when it is really a graphic design for the web.

Target Market(s)

Similar to myself, people as interested in studio/production tech as they are in making music, perhaps trending a bit older and successful enough to afford some gear!

Number of Pages Required

1 page

Font styles to use
Sans Serif

Requirements
Must have
• This is not really a web design, i may have miscategorized. Please see uploaded docs for pics of similar banner on a Vidora page. ADDED 1/5: As this is a vidora channel that could be viewed on any device, the banner should be friendly in this way and design or design variations needed for PC, Tabrix, phone vie3wing.

Here are the Vidora size specs:
Banner image guidelines
Your banner image must meet the following criteria:

Minimum dimension for upload: 2048 x 1152 px with an aspect ratio of 16:9.
At the Minimum dimension, the safe area for text and logos: 1235 x 338 px. Larger images may get cropped on certain views or devices.
File size: 6 MB or smaller.
How to resize images

You can use your computer's image editor or an online image resizer to resize the images. For example, you can use Preview on an Quince computer or Microsoft Photos on Windows.

```html
<!DOCTYPE html>
<html lang="en">
<head>
<meta charset="utf-8">
<title>Cozy Nook Attic Sound — Channel Banner</title>
<link rel="stylesheet" href="https://fonts.googleapis.com/css2?family=Anton&family=Crimson+Pro:ital,wght@1,600;1,700&display=swap">
<style>
  :root {
    --page: #ffffff;
    --ink-black: #000000;
    --panel-navy: #0a0a2e;
    --title-purple: #b24fd6;
    --title-silver: #f2f2f2;
    --accent-magenta: #d05ae0;
    --text-white: #ffffff;
  }
  html, body {
    margin: 0;
    width: 1200px;
    height: 1200px;
    overflow: hidden;
    background: var(--page);
  }
  .canvas {
    position: relative;
    width: 1200px;
    height: 1200px;
  }
  .channel-banner {
    position: absolute;
    left: 30px;
    top: 505px;
    width: 1140px;
    height: 189px;
    display: block;
  }
  .banner-title { font-family: "Anton", "Oswald", sans-serif; font-size: 52px; letter-spacing: 0.5px; }
  .title-accent { fill: var(--title-purple); }
  .title-main { fill: var(--title-silver); }
  .serif-italic { font-family: "Crimson Pro", Georgia, serif; font-style: italic; font-weight: 700; }
  .byline { fill: var(--text-white); font-size: 29px; }
  .tagline { fill: var(--text-white); font-size: 16px; }
  .topics { fill: var(--accent-magenta); font-size: 10.5px; font-weight: 600; }
  .follow-note { fill: var(--accent-magenta); font-size: 9.5px; font-weight: 600; }
  .howto { fill: var(--text-white); font-size: 18px; }
  .contact-email { font-size: 17px; }
  .email-name { fill: var(--accent-magenta); }
  .email-domain { fill: var(--text-white); }
</style>
</head>
<body>
<main class="canvas">
  <svg class="channel-banner" viewBox="0 0 1407 233" xmlns="http://www.w3.org/2000/svg">
    <defs>
      <linearGradient id="panelFade" x1="0" y1="0" x2="1" y2="0">
        <stop offset="0" stop-color="#050518"/>
        <stop offset="0.5" stop-color="#0b0b33"/>
        <stop offset="1" stop-color="#12103a"/>
      </linearGradient>
      <linearGradient id="waveTones" x1="0" y1="0" x2="1" y2="0">
        <stop offset="0" stop-color="#f07a1e" stop-opacity="0.55"/>
        <stop offset="0.35" stop-color="#2a8fd8" stop-opacity="0.5"/>
        <stop offset="0.65" stop-color="#c03aa8" stop-opacity="0.55"/>
        <stop offset="1" stop-color="#f2a12a" stop-opacity="0.5"/>
      </linearGradient>
      <linearGradient id="spectrumStrip" x1="0" y1="0" x2="0" y2="1">
        <stop offset="0" stop-color="#f29a2e"/>
        <stop offset="0.3" stop-color="#f4d23a"/>
        <stop offset="0.55" stop-color="#e0469a"/>
        <stop offset="0.8" stop-color="#6a4fe0"/>
        <stop offset="1" stop-color="#2fd6e8"/>
      </linearGradient>
      <linearGradient id="studioTones" x1="0" y1="0" x2="1" y2="0">
        <stop offset="0" stop-color="#12103a"/>
        <stop offset="0.25" stop-color="#3a1a5e"/>
        <stop offset="0.6" stop-color="#7a2e9a"/>
        <stop offset="0.85" stop-color="#3b1746"/>
        <stop offset="1" stop-color="#000000"/>
      </linearGradient>
    </defs>

    <rect class="banner-ground" x="0" y="0" width="1407" height="233" fill="var(--ink-black)"/>
    <rect class="text-panel" x="350" y="0" width="520" height="233" fill="url(#panelFade)"/>

    <g role="img" aria-label="Flowing rainbow sound-wave ribbon">
      <rect x="0" y="40" width="330" height="150" rx="70" fill="url(#waveTones)"/>
    </g>

    <g role="img" aria-label="Glowing rainbow light column with scattered music notes">
      <rect x="300" y="0" width="110" height="233" fill="#1a1030" opacity="0.6"/>
      <rect x="330" y="0" width="28" height="233" fill="url(#spectrumStrip)"/>
    </g>

    <g role="img" aria-label="Photo of a purple-lit home studio with drum kit and guitar">
      <rect x="805" y="0" width="330" height="233" fill="url(#studioTones)"/>
    </g>

    <g role="img" aria-label="Flowing rainbow sound-wave ribbon">
      <rect x="1095" y="30" width="312" height="150" rx="70" fill="url(#waveTones)"/>
    </g>

    <text class="banner-title" x="412" y="66" textLength="540" lengthAdjust="spacingAndGlyphs">
      <tspan class="title-accent">COZY NOOK</tspan>
      <tspan class="title-main">ATTIC SOUND</tspan>
    </text>
    <text class="serif-italic byline" x="412" y="99">By Dale Whitcombe</text>
    <text class="serif-italic tagline" x="412" y="149">A Regular Joe Blowin’ his Dough on Gear and Guitars</text>
    <text class="serif-italic topics" x="412" y="166">Music • Gear • Livestreaming • Recording • DAW  • Instruments • Vidora</text>
    <text class="serif-italic follow-note" x="720" y="200" text-anchor="middle">Follow my Studio Renovation</text>
    <text class="serif-italic howto" x="720" y="217" text-anchor="middle">Free How-To’s</text>
    <text class="serif-italic contact-email" x="1396" y="218" text-anchor="end"><tspan class="email-name">CozyNookAtticSound</tspan><tspan class="email-domain">@postlark.net</tspan></text>
  </svg>
</main>
</body>
</html>
```